Missed checkup for a dental appointment

Postcard as a follow up when a patient has not mad an appointment in line wiht their 6 monthly text reminder.

opiton1
cosmetic family orientated, happy, beautiful smiles, beautiful people. something like "it's time to get back on track with your dental health visit at Brenlow Tooth Studio (formerly Perry Halvick Dental)" or "You are due a oral health check and clean at Brenlow Tooth Studio (formerly Perry Halvick Dental)" POSSIBLY WITH A BIG A PLUS FOR HEALTH CHECK EXAM OR TICK or "A lot has changed Come and See the New Place at Brenlow Tooth Studio (formerly Perry Halvick Dental), or "We It's been a while, miss you, give us a call and come in for your check at Brenlow Tooth Studio (formerly Perry Halvick Dental) POSSIBLY WIHT A PICTURE OF A RUNNER BEAN AND TOOTH BRUSH
OR "it's been a tough year let's get back to health before it gets back at you! call for your Dental Check today!" maybe with a picture of spots of blood in the wash basin or on a tooth brush
OR "Stay ahead wiht your health DON'T WAIT " wiht a picture of someone hit a missing tooth in front of three mouth.

ALL postcards must have our details and a call to action very prominent
Above Tuv bank
Unit 9 Corrimal ridge road
Airlie Beach
Qld
4802

47215938 CALL NOW

Sick

Target Market(s)

matriachical mother 30-70 y old inline with how the logo was deigned

Industry/Entity Type

Dental

Requirements
Must have
• call to action urgency
• phone number 47215983
• practice logo on cards
Nice to have
• thought provoking pictures either funny or double-entendres with the words , memorable, or deeply thought provoking making a patient realise the importance of their health or the importance of using their benefit or the importance of regular early checkups
Should not have
• no blood pictures
• Wrong phone numbers
• No fat cats
• No 2017
• No use up benifits

```html
<!DOCTYPE html>
<html lang="en">
<head>
<meta charset="utf-8">
<title>Brenlow Tooth Studio – Dental Check Postcard</title>
<link rel="stylesheet" href="https://fonts.googleapis.com/css2?family=Inter:wght@200;300;600&display=swap">
<style>
  :root {
    --paper: #ffffff;
    --green: #8cc541;
    --green-shade: #5a8d34;
    --blue-deep: #0879ae;
    --blue-mid: #1e9dcd;
    --teal: #62b3bb;
    --teal-dark: #4a9b8c;
    --sky-text: #86d2f2;
    --white: #ffffff;
    --brand-blue: #0aa6e2;
    --photo-light: #e9eef1;
    --photo-mid: #c9d3da;
    --photo-warm: #e8b08a;
    --photo-dark: #2a2a2a;
  }
  * { margin: 0; padding: 0; box-sizing: border-box; }
  html, body {
    width: 1200px; height: 930px; overflow: hidden;
    background: var(--paper);
    font-family: "Inter", "Helvetica Neue", Arial, sans-serif;
  }
  .canvas { position: relative; width: 1200px; height: 930px; }

  .postcard {
    position: absolute; left: 12px; top: 13px;
    width: 564px; height: 748px;
    overflow: hidden;
    border-bottom-right-radius: 64px;
    border: 1px solid #a9d27a;
    border-bottom: none; border-right: none;
  }
  .postcard__photo {
    position: absolute; left: 0; top: 0; width: 564px; height: 375px;
    background:
      radial-gradient(ellipse 45% 55% at 75% 45%, var(--photo-warm) 0%, rgba(232,176,138,0) 70%),
      radial-gradient(ellipse 30% 60% at 92% 40%, var(--photo-dark) 0%, rgba(42,42,42,0) 75%),
      linear-gradient(120deg, var(--photo-light) 0%, var(--photo-mid) 55%, #f2f4f6 100%);
  }
  .postcard__shapes { position: absolute; left: 0; top: 0; }

  .headline {
    position: absolute; left: 31px; top: 390px;
    color: var(--white);
    font-weight: 200; font-size: 37px; line-height: 46px;
    letter-spacing: -1.2px;
  }
  .cta {
    position: absolute; left: 31px; top: 544px;
    color: var(--sky-text);
    font-weight: 600; font-size: 25px; letter-spacing: -0.2px;
  }
  .phone {
    position: absolute; left: 29px; top: 584px;
    color: var(--sky-text);
    font-weight: 200; font-size: 53px; letter-spacing: -1px;
  }
  .practice-name {
    position: absolute; left: 31px; top: 649px;
    color: var(--white);
    font-weight: 600; font-size: 28px;
  }
  .address {
    position: absolute; left: 31px; top: 685px;
    color: var(--white);
    font-weight: 300; font-size: 22px; line-height: 28px;
  }

  .brand {
    position: absolute; left: 612px; top: 142px;
    display: flex; align-items: center; gap: 14px;
  }
  .brand__dot {
    width: 52px; height: 52px; border-radius: 50%;
    background: var(--brand-blue);
  }
  .brand__name {
    color: var(--brand-blue);
    font-weight: 600; font-size: 30px; letter-spacing: -0.5px;
  }
</style>
</head>
<body>
<main class="canvas">
  <section class="postcard">
    <div class="postcard__photo" role="img" aria-label="Dentist in protective glasses using a curing light on a female patient"></div>

    <svg class="postcard__shapes" width="564" height="748" viewBox="0 0 564 748" aria-hidden="true">
      <rect x="0" y="520" width="564" height="228" fill="var(--blue-deep)"/>
      <polygon points="564,536 564,748 180,748" fill="var(--blue-mid)"/>
      <polygon points="564,603 564,748 0,748 0,739" fill="var(--teal)"/>
      <polygon points="0,739 360,655 180,748 0,748" fill="var(--teal-dark)" opacity="0.7"/>
      <path d="M0,379 H564 V471 Q564,535 500,535 H0 Z" fill="var(--green-shade)"/>
      <path d="M0,375 H564 V467 Q564,531 500,531 H0 Z" fill="var(--green)"/>
    </svg>

    <h1 class="headline">It's been a tough year.<br>let's get back to health<br>before it gets back at you!</h1>
    <p class="cta">Call for your Dental Check today!</p>
    <p class="phone">47215938</p>
    <h2 class="practice-name">Brenlow Tooth Studio</h2>
    <p class="address">Above Tuv bank, Unit 9 Corrimal ridge road<br>Marlow Cove, Qld - 4819</p>
  </section>

  <div class="brand">
    <span class="brand__dot" aria-hidden="true"></span>
    <span class="brand__name">Brenlow Tooth Studio</span>
  </div>
</main>
</body>
</html>
```